EYE CATCHING Tralvoni And Website Banner Ads

I am a boutique real-estate agency in Brisbane Australia. I need an eye catching banner ad design for tralvoni and also other website.Color scheme must be the same as logo but must use eye catching text and images to draw people to clickSee brochure ads for inspirationBanner sizes as follows1200x628 pixel (tralvoni)728x90 pixel472x114 pixel300x600 pixel160x600 pixel

Target Market(s)

Home Owners

Industry/Entity Type

Real Estate Agent

Colors

Designer to choose colors to be used in the design.

Requirements
Must have
• It is very important designs must be clear and easy to read
• Each ad MUST have a call to action button "Learn More"
• Color scheme must be the same as logo
• Must be Eye catching
• Must convey trustworthiness and professionalism
• Must be different to all the other real estate ads! A little modern!
Should not have
• Must not be cluttered and too busy

```html
<!DOCTYPE html>
<html lang="en">
<head>
<meta charset="utf-8">
<title>Harbourline Realty – Full Service Banner</title>
<link href="https://fonts.googleapis.com/css2?family=Montserrat:wght@500;600;800;900&display=swap" rel="stylesheet">
<style>
  :root {
    --navy: #0e2846;
    --navy-deep: #0a1f38;
    --accent-blue: #1562ae;
    --ribbon-blue: #1d5598;
    --sky: #a9d8ff;
    --sky-edge: #3a8fd8;
    --white: #ffffff;
    --soft-white: #e9edf2;
    --gap: #f4f6f9;
  }
  * { margin: 0; padding: 0; box-sizing: border-box; }
  html, body { width: 1200px; height: 900px; overflow: hidden; background: var(--gap); }
  body { font-family: "Montserrat", Arial, sans-serif; position: relative; }

  .banner { position: absolute; left: 0; width: 1200px; background: var(--navy); overflow: hidden; }
  .banner--wide { top: 0; height: 628px; }
  .banner--preview { top: 632px; height: 268px; }

  .headline-word {
    position: absolute; left: 46px;
    font-weight: 900; color: var(--soft-white);
    line-height: 1; letter-spacing: 1px;
    text-shadow: 0 3px 0 #b9c2cc, 0 7px 10px rgba(0,0,0,0.55);
  }
  .headline-word--full { top: 44px; font-size: 66px; }
  .headline-word--service { top: 126px; font-size: 66px; }
  .headline-word--agency { top: 208px; font-size: 66px; }
  .headline-word--commission { top: 286px; font-size: 81px; letter-spacing: 0; }

  .percent {
    position: absolute; left: 370px; top: 8px;
    font-size: 300px; font-weight: 900; line-height: 1;
    color: var(--sky); letter-spacing: -14px;
    text-shadow: 5px 4px 0 var(--sky-edge), 10px 10px 14px rgba(0,0,0,0.5);
  }

  .ribbon {
    position: absolute; left: 194px; top: 380px; width: 448px; height: 43px;
    background: var(--ribbon-blue);
    clip-path: polygon(16px 0, 100% 0, calc(100% - 16px) 100%, 0 100%);
    color: var(--white); font-weight: 600; font-size: 23px;
    display: flex; align-items: center; justify-content: center;
  }

  .contact-label { position: absolute; left: 46px; top: 453px; font-size: 31px; font-weight: 500; color: var(--soft-white); }
  .contact-phone { position: absolute; left: 46px; top: 494px; font-size: 52px; font-weight: 800; color: var(--sky); letter-spacing: 4px; }
  .contact-email { position: absolute; left: 48px; top: 563px; font-size: 19px; font-weight: 500; color: var(--soft-white); }

  .cta {
    position: absolute; left: 495px; top: 532px; width: 175px; height: 48px;
    border-radius: 24px;
    background: linear-gradient(#4a6f98, #1b3d63 55%, #14324f);
    box-shadow: 0 4px 8px rgba(0,0,0,0.5), inset 0 1px 0 rgba(255,255,255,0.4);
    color: var(--white); font-size: 15px; font-weight: 500;
    display: flex; align-items: center; justify-content: center; gap: 10px;
  }

  .showcase { position: absolute; left: 0; top: 0; width: 1200px; height: 628px; }

  .brand-name {
    position: absolute; left: 960px; top: 62px; width: 200px;
    text-align: center; color: var(--white);
    font-weight: 600; font-size: 24px; line-height: 1.15; letter-spacing: 1px;
  }

  .preview-word {
    position: absolute; left: 108px; font-size: 112px; font-weight: 900; line-height: 1;
    color: var(--soft-white);
    text-shadow: 0 4px 0 #b9c2cc, 0 9px 12px rgba(0,0,0,0.55);
  }
  .preview-word--full { top: 28px; }
  .preview-word--service { top: 150px; }
  .preview-percent {
    position: absolute; left: 600px; top: 0px;
    font-size: 440px; font-weight: 900; line-height: 1;
    color: var(--sky); letter-spacing: -20px;
    text-shadow: 7px 6px 0 var(--sky-edge), 14px 14px 18px rgba(0,0,0,0.5);
  }
</style>
</head>
<body>

<section class="banner banner--wide">
  <svg class="showcase" viewBox="0 0 1200 628" aria-hidden="false">
    <defs>
      <clipPath id="photo-clip"><circle cx="1300" cy="310" r="525"/></clipPath>
      <linearGradient id="sky-house" x1="0" y1="0" x2="0" y2="1">
        <stop offset="0" stop-color="#3f7fd0"/>
        <stop offset="0.35" stop-color="#b9d6f2"/>
        <stop offset="0.45" stop-color="#eef1f4"/>
        <stop offset="1" stop-color="#dcdfe2"/>
      </linearGradient>
      <linearGradient id="interior" x1="0" y1="0" x2="0" y2="1">
        <stop offset="0" stop-color="#f3f4f5"/>
        <stop offset="0.6" stop-color="#d9d6d0"/>
        <stop offset="1" stop-color="#b08a66"/>
      </linearGradient>
    </defs>
    <circle cx="1300" cy="310" r="550" fill="var(--accent-blue)"/>
    <g clip-path="url(#photo-clip)">
      <rect x="760" y="0" width="440" height="468" fill="url(#sky-house)" role="img" aria-label="Photo of a white two-storey weatherboard home under a blue sky"/>
      <rect x="760" y="468" width="440" height="4" fill="var(--white)"/>
      <rect x="760" y="472" width="231" height="156" fill="url(#interior)" role="img" aria-label="Photo of a bright living room with grey sofas and timber floors"/>
      <rect x="991" y="472" width="4" height="156" fill="var(--white)"/>
      <rect x="995" y="472" width="205" height="156" fill="url(#interior)" role="img" aria-label="Photo of a dining area with a white table and woven chairs"/>
    </g>
  </svg>

  <div class="brand-name">HARBOURLINE<br>REALTY</div>

  <h1>
    <span class="headline-word headline-word--full">FULL</span>
    <span class="headline-word headline-word--service">SERVICE</span>
    <span class="headline-word headline-word--agency">AGENCY</span>
    <span class="headline-word headline-word--commission">COMMISSION</span>
  </h1>
  <div class="percent">1%</div>

  <div class="ribbon">MORE MONEY IN YOUR POCKET</div>

  <p class="contact-label">CONTACT MARCUS TODAY</p>
  <p class="contact-phone">0400.123.987</p>
  <p class="contact-email">marcus@harbourlinerealty.com.au</p>

  <a class="cta">
    <svg width="24" height="22" viewBox="0 0 24 22" fill="none" stroke="#fff" stroke-width="1.8" aria-hidden="true">
      <path d="M8 6V2h14v18H8v-4"/>
      <path d="M1 11h13M10 7l4 4-4 4"/>
    </svg>
    Learn More
  </a>
</section>

<section class="banner banner--preview">
  <span class="preview-word preview-word--full">FULL</span>
  <span class="preview-word preview-word--service">SERVICE</span>
  <span class="preview-percent">1%</span>
</section>

</body>
</html>
```